Allied Health team of Physiotherapists & Occupational Therapists seek a business card design

We have our new logo, we now need our new business cards and stationary. Blossom: Lymphoedema & Women's Clinic is seeking a generic card design to represent our whole team and individual cards for each therapist that incorporates our new logo to communicate our holistic approach that is calming, nuturing, supportive and welcoming.
Our Physiotherapists and Occupational Therapists assess, treat and provide education for people who are at risk of or who have lymphoedema. This is often as a result of treatment for cancer. We provide pre-operative and post-operative management and cancer rehabilitation in our Pilates studio. Our team also consists of Physiotherapists who have a strong interest in pelvic floor and continence management for both men and women.

Target Market(s)

Mainly women health conscious

Industry/Entity Type

Allied Health: Physiotherapy / Occupational Therapy

Contact Information for Business Card

Address: 14 Calloway Ave Larkfield 3287 Phone: 84317560 fax: 8431 7564 Email: info@blossomcarepartners.com.au Website: blossomcarepartners.com.au Facebook address: facebook.com/BlossomLymphoedemaAndWomensCareCentre. Room to write appointments. Individual cards need to have name, office email and individual email and professional details

Requirements
Must have
• Logo as per uploaded documents

```html
<!DOCTYPE html>
<html lang="en">
<head>
<meta charset="utf-8">
<title>Blossom Clinic – Business Card &amp; Appointment Card</title>
<link href="https://fonts.googleapis.com/css2?family=Jost:wght@400;500&family=Nunito:wght@800&family=Montserrat:ital,wght@0,500;1,500;1,800&display=swap" rel="stylesheet">
<style>
  :root {
    --backdrop: #e4e4e4;
    --cream: #f5e9df;
    --peach: #f9af7e;
    --peach-text: #f6a978;
    --sage: #c2ccbd;
    --white: #ffffff;
    --note-grey: #555555;
  }
  * { margin: 0; padding: 0; box-sizing: border-box; }
  html, body { width: 1200px; height: 933px; overflow: hidden; background: var(--backdrop); }
  body { position: relative; font-family: "Jost", sans-serif; }

  .card { position: absolute; background: var(--cream); border-radius: 16px; overflow: hidden;
          box-shadow: 0 10px 22px rgba(0,0,0,0.18); }

  /* Front card */
  .card-front { left: 135px; top: 145px; width: 305px; height: 533px; }
  .card-front .wave { position: absolute; left: 0; top: 0; width: 305px; height: 533px; }
  .brand-mark { position: absolute; left: 0; top: 120px; width: 305px; display: flex;
                justify-content: center; align-items: center; gap: 8px; }
  .brand-mark .dot { width: 10px; height: 10px; border-radius: 50%; background: var(--peach); }
  .brand-mark .brand-name { font-family: "Jost", sans-serif; font-weight: 400; font-size: 40px;
                            color: var(--peach); letter-spacing: 1px; }
  .details { position: absolute; left: 40px; top: 340px; color: var(--white); }
  .details .person { font-family: "Nunito", sans-serif; font-weight: 800; font-size: 21px; line-height: 1.1; }
  .details .role { font-size: 12.5px; margin-top: 1px; }
  .details .rule { width: 28px; height: 1.5px; background: var(--white); margin: 12px 0 10px; }
  .details .contact { font-size: 13.5px; line-height: 17px; }
  .details .address { font-size: 13.5px; }

  /* Back card */
  .card-back { left: 535px; top: 259px; width: 533px; height: 305px; color: var(--peach-text); }
  .watermark { position: absolute; left: 0; top: 120px; width: 533px; text-align: center;
               font-size: 64px; color: var(--peach); opacity: 0.12; }
  .appt-title { position: absolute; left: 37px; top: 26px; font-family: "Montserrat", sans-serif;
                font-weight: 500; font-size: 20.5px; }
  .book-online { position: absolute; left: 396px; top: 34px; width: 103px; height: 21px;
                 background: var(--peach); border-radius: 6px; color: var(--white);
                 font-family: "Montserrat", sans-serif; font-style: italic; font-weight: 800;
                 font-size: 12.5px; display: flex; align-items: center; justify-content: center; }
  .field-row { position: absolute; left: 36px; right: 37px; display: flex; align-items: flex-end;
               font-size: 13px; gap: 6px; }
  .field-row .fill { flex: 1; border-bottom: 1.5px dotted var(--peach-text); height: 10px; }
  .row-name { top: 72px; right: 48px; }
  .row-date { top: 109px; right: 55px; }
  .row-note { top: 180px; }
  .row-extra { top: 210px; }
  .days { position: absolute; left: 36px; top: 150px; width: 450px; display: flex;
          justify-content: space-between; font-size: 13px; }
  .day { display: flex; align-items: center; gap: 6px; }
  .day .box { width: 13px; height: 10px; border: 1px solid var(--peach-text); opacity: 0.6; }
  .notice { position: absolute; left: 0; top: 246px; width: 533px; text-align: center;
            font-family: "Montserrat", sans-serif; font-style: italic; font-size: 11.5px;
            line-height: 15px; color: var(--note-grey); }
</style>
</head>
<body>

<section class="card card-front">
  <svg class="wave" viewBox="0 0 305 533" aria-hidden="true">
    <path d="M0 235 Q152 350 305 255 L305 533 L0 533 Z" fill="var(--sage)"/>
    <path d="M0 258 Q150 335 305 255 L305 533 L0 533 Z" fill="var(--white)"/>
    <path d="M0 262 Q150 338 305 259 L305 533 L0 533 Z" fill="var(--peach)"/>
  </svg>
  <div class="brand-mark">
    <span class="dot"></span>
    <span class="brand-name">Blossom</span>
  </div>
  <div class="details">
    <p class="person">Maren Ashby</p>
    <p class="role">Physiotherapist</p>
    <div class="rule"></div>
    <p class="contact">(P) 8431 7560</p>
    <p class="contact">(F) 8431 7564</p>
    <p class="contact">info@blossomcarepartners.com.au</p>
    <div class="rule"></div>
    <p class="address">14 Calloway Ave, Larkfield 3287</p>
  </div>
</section>

<section class="card card-back">
  <div class="watermark" aria-hidden="true">Blossom</div>
  <h2 class="appt-title">Next Appointment</h2>
  <div class="book-online">Book Online</div>
  <div class="field-row row-name"><span>Name :</span><span class="fill"></span></div>
  <div class="field-row row-date"><span>Date :</span><span class="fill"></span><span>Time :</span><span class="fill" style="flex:0 0 110px"></span><span style="font-size:11px">AM/PM</span></div>
  <div class="days">
    <span class="day"><span class="box"></span>Sun</span>
    <span class="day"><span class="box"></span>Mon</span>
    <span class="day"><span class="box"></span>Tue</span>
    <span class="day"><span class="box"></span>Wed</span>
    <span class="day"><span class="box"></span>Thu</span>
    <span class="day"><span class="box"></span>Fri</span>
    <span class="day"><span class="box"></span>Sat</span>
  </div>
  <div class="field-row row-note"><span>Note :</span><span class="fill"></span></div>
  <div class="field-row row-extra"><span class="fill"></span></div>
  <p class="notice">Please give me 24 hours notice if you are unable to keep your appointment or<br>a cancellation fee may be charged.</p>
</section>

</body>
</html>
```